Brochure Design Project

This will be a tri-fold full 8.5x11 brochure that will be distributed and sitting in Oncology offices all throughout the US. It is a lead generation and referral designed piece that it to target all patients, Cancer primarily, but all critically ill patients and seniors above the age of 70. We want our service to go beyond just a financial transaction, we want to educate patients of their rights within a life insurance policy and if we cannot help them personally, do want to assist them by referring them to other agencies and non profits than can. ( I want to redesign the brochure attached, it can be very similar and need only minor changes to content, but would welcome all suggestions on improving message, and in gaining attention, picture substitutions and change of colors, along with the layout itself can be improved upon, and I need this piece to look very professional and appropriate for medical offices. I will be needing assistance on several upcoming projects and will also have great printing demands.

Target Market(s)

Cancer patients
all chronically and critically ill patients
all seniors above age 70

Industry/Entity Type

Life Insurance

Requirements
Must have
• Cancer and the terminally ill
Nice to have
• seniors above 70

```html
<!DOCTYPE html>
<html lang="en">
<head>
<meta charset="utf-8">
<title>Life Insurance Options Brochure</title>
<link rel="stylesheet" href="https://fonts.googleapis.com/css2?family=Montserrat:wght@400;600;700;800&family=Mulish:wght@400;600&display=swap">
<style>
  :root {
    --sky-top: #ffffff;
    --sky-mid: #e6f5fd;
    --sky-edge: #b7e2f7;
    --lime: #a3c639;
    --pink: #ec6aa5;
    --magenta: #e8237e;
    --emerald: #1ba356;
    --navy: #2e3192;
    --ink: #111111;
    --grey: #7a7a7a;
    --swoosh: #5fb7e8;
    --swoosh-light: #a9d9f3;
    --white: #ffffff;
  }
  * { margin: 0; padding: 0; box-sizing: border-box; }
  html, body { width: 1200px; height: 933px; overflow: hidden; background: var(--white); }
  .brochure {
    position: relative;
    width: 1200px; height: 933px; overflow: hidden;
    background: linear-gradient(100deg, var(--sky-top) 0%, var(--sky-mid) 45%, var(--sky-edge) 100%);
    font-family: "Mulish", "Helvetica Neue", Arial, sans-serif;
  }
  .heading {
    position: absolute;
    font-family: "Montserrat", Arial, sans-serif;
    font-weight: 700;
    font-size: 37px;
    line-height: 1;
    white-space: nowrap;
  }
  .copy {
    position: absolute;
    font-size: 13.2px;
    line-height: 13.9px;
    letter-spacing: 0.3px;
    text-align: justify;
    hyphens: none;
  }
  .photo-area { position: absolute; left: 0; top: 0; width: 500px; height: 450px; }

  /* middle column */
  .heading--everyone { left: 556px; top: 158px; color: var(--emerald); }
  .copy--everyone { left: 421px; top: 196px; width: 358px; color: var(--ink); text-align-last: right; }
  .copy--everyone .wrap-shape {
    float: left; width: 130px; height: 270px;
    shape-outside: polygon(0 0, 100% 0, 90% 15%, 72% 35%, 45% 55%, 15% 72%, 0 80%);
  }
  .heading--help { left: 424px; top: 510px; color: var(--magenta); }
  .copy--help { left: 421px; top: 556px; width: 358px; color: var(--ink); }
  .tagline {
    position: absolute; left: 421px; top: 812px;
    font-family: "Montserrat", Arial, sans-serif; font-weight: 700;
    font-size: 21px; line-height: 1.2; color: var(--magenta); white-space: nowrap;
  }

  /* left column */
  .heading--money { left: 26px; top: 482px; color: var(--navy); }
  .copy--money { left: 26px; top: 527px; width: 343px; color: var(--grey); }

  .footer-shapes { position: absolute; left: 0; top: 790px; width: 800px; height: 143px; }
  .footer-message {
    position: absolute; left: 12px; top: 829px; width: 370px;
    text-align: center; color: var(--white);
    font-family: "Montserrat", Arial, sans-serif; font-weight: 700;
    font-size: 17px; line-height: 18px;
  }
  .phone {
    position: absolute; display: flex; align-items: center; gap: 6px;
    font-family: "Montserrat", Arial, sans-serif; font-weight: 400;
    color: var(--white); white-space: nowrap; line-height: 1;
  }
  .phone svg { flex: none; }
  .phone--footer { left: 443px; top: 880px; font-size: 39px; }

  /* right panel */
  .info-box {
    position: absolute; left: 809px; top: 0; width: 365px; height: 471px;
    background: var(--lime);
  }
  .copy--info { left: 11px; top: 93px; width: 344px; color: var(--white); line-height: 13.2px; }
  .phone--info { left: 7px; top: 405px; font-size: 42px; }
  .data-area {
    position: absolute; left: 905px; top: 491px; width: 170px; height: 272px;
    display: flex; align-items: flex-end; justify-content: center;
  }
  .data-area span {
    display: block;
    font-family: "Montserrat", Arial, sans-serif; font-weight: 800;
    font-size: 82px; line-height: 80px; letter-spacing: 3px;
    color: rgba(255,255,255,0.6);
    transform: rotate(-90deg); transform-origin: center;
    white-space: nowrap; text-align: left;
  }
</style>
</head>
<body>
<main class="brochure">

  <svg class="photo-area" viewBox="0 0 500 450" role="img" aria-label="Photograph of a smiling senior couple embracing">
    <defs>
      <linearGradient id="photoFill" x1="0" y1="0" x2="1" y2="1">
        <stop offset="0" stop-color="#eceae6"/>
        <stop offset="0.5" stop-color="#d9d2ca"/>
        <stop offset="1" stop-color="#c7c4c2"/>
      </linearGradient>
    </defs>
    <path d="M0 0 H420 C470 40 480 150 460 260 C440 360 380 420 250 420 C150 420 60 400 0 370 Z" fill="url(#photoFill)"/>
    <path d="M0 370 C90 420 210 445 330 425 C420 410 470 330 480 230 C488 140 470 60 440 20 C470 90 470 200 440 290 C400 390 300 420 200 410 C110 400 40 380 0 350 Z" fill="var(--swoosh-light)" opacity="0.8"/>
    <path d="M60 395 C160 440 290 445 380 400 C450 360 490 260 480 150 C500 260 470 370 390 420 C300 460 160 445 60 395 Z" fill="var(--swoosh)"/>
    <path d="M440 10 C490 90 500 210 470 300" stroke="var(--white)" stroke-width="1.5" fill="none"/>
  </svg>

  <h2 class="heading heading--everyone">Everyone</h2>
  <p class="copy copy--everyone"><span class="wrap-shape"></span>Lorem ipsum dolor sit amet, consectetur adipiscing elit. Sed malesuada erat in commodo tristique. Nam et feugiat justo. Phasellus a pulvinar purus. Fusce viverra, turpis iaculis auctor imperdiet, enim massa porta dui, at placerat tellus erat sit amet sapien. Vestibulum et pretium nisl. Duis pulvinar metus eu leo dignissim blandit. Fusce egestas est sed mauris consequat semper viverra non tortor. Etiam rhoncus interdum sem, eu gravida diam posuere vitae. Vivamus ante tortor, tempus id enim at, mollis malesuada eros. Fusce id dapibus mauris, a consequat libero. Curabitur imperdiet, sapien vel accumsan commodo, lectus felis tincidunt libero, eget eleifend lectus ipsum vel ligula. Phasellus sed nunc elementum, fermentum massa porta, tincidunt massa. Aliquam nec interdum arcu.</p>

  <h2 class="heading heading--money">It`s Your money</h2>
  <p class="copy copy--money">Lorem ipsum dolor sit amet, consectetur adipiscing elit. Sed malesuada erat in commodo tristique. Nam et feugiat justo. Phasellus a pulvinar purus. Fusce viverra, turpis iaculis auctor imperdiet, enim massa porta dui, at placerat tellus erat sit amet sapien. Vestibulum et pretium nisl. Duis pulvinar metus eu leo dignissim blandit. Fusce egestas est sed mauris consequat semper viverra non tortor. Etiam rhoncus interdum sem, eu gravida diam posuere vitae. Vivamus ante tortor, tempus id enim at, mollis malesuada eros. Fusce id dapibus mauris, a consequat libero. Curabitur imperdiet, sapien vel accumsan commodo, lectus felis tincidunt libero, eget eleifend lectus ipsum vel ligula. Phasellus sed nunc elementum, fermentum massa porta, tincidunt massa. Aliquam nec interdum arcu.</p>

  <h2 class="heading heading--help">We Can Help</h2>
  <p class="copy copy--help">Lorem ipsum dolor sit amet, consectetur adipiscing elit. Sed malesuada erat in commodo tristique. Nam et feugiat justo. Phasellus a pulvinar purus. Fusce viverra, turpis iaculis auctor imperdiet, enim massa porta dui, at placerat tellus erat sit amet sapien. Vestibulum et pretium nisl. Duis pulvinar metus eu leo dignissim blandit. Fusce egestas est sed mauris consequat semper viverra non tortor. Etiam rhoncus interdum sem, eu gravida diam posuere vitae. Vivamus ante tortor, tempus id enim at, mollis malesuada eros. Fusce id dapibus mauris, a consequat libero. Curabitur imperdiet, sapien vel accumsan commodo, lectus felis tincidunt libero, eget eleifend lectus ipsum vel ligula. Phasellus sed nunc elementum, fermentum massa porta, tincidunt massa. Aliquam nec interdum arcu.</p>

  <svg class="footer-shapes" viewBox="0 0 800 143" aria-hidden="true">
    <path d="M0 41 C60 20 180 10 260 25 C350 45 420 70 457 83 C300 95 160 115 83 143 H0 Z" fill="var(--lime)"/>
    <path d="M436 92 C560 80 680 72 795 70 V143 H436 Z" fill="var(--pink)"/>
    <path d="M343 80 C480 70 640 64 795 66" stroke="var(--white)" stroke-width="2.5" fill="none"/>
  </svg>

  <p class="tagline">Turn ing “HOPE” into reality</p>
  <p class="footer-message">Healing &amp; recovery should be<br>the primary concern for all patient<br>“Not Money” or “The Lack Of”</p>

  <div class="phone phone--footer">
    <svg width="34" height="30" viewBox="0 0 34 30" aria-hidden="true"><path d="M3 9 C3 3 31 3 31 9 L28 12 L23 10 L23 7 C19 6 15 6 11 7 L11 10 L6 12 Z M9 13 L25 13 L30 27 H4 Z M17 16 a4.5 4.5 0 1 0 0.01 0 Z" fill="rgba(255,255,255,0.6)" fill-rule="evenodd"/></svg>
    <span>800-555-1212</span>
  </div>

  <section class="info-box">
    <p class="copy copy--info">Lorem ipsum dolor sit amet, consectetur adipiscing elit. Sed malesuada erat in commodo tristique. Nam et feugiat justo. Phasellus a pulvinar purus. Fusce viverra, turpis iaculis auctor imperdiet, enim massa porta dui, at placerat tellus erat sit amet sapien. Vestibulum et pretium nisl. Duis pulvinar metus eu leo dignissim blandit. Fusce egestas est sed mauris consequat semper viverra non tortor. Etiam rhoncus interdum sem, eu gravida diam posuere vitae. Vivamus ante tortor, tempus id enim at, mollis malesuada eros. Fusce id dapibus mauris, a consequat libero. Curabitur imperdiet, sapien vel accumsan commodo, lectus felis tincidunt libero, eget eleifend lectus ipsum vel ligula. Phasellus sed nunc elementum, fermentum massa porta, tincidunt massa. Aliquam nec interdum arcu.</p>
    <div class="phone phone--info">
      <svg width="36" height="32" viewBox="0 0 34 30" aria-hidden="true"><path d="M3 9 C3 3 31 3 31 9 L28 12 L23 10 L23 7 C19 6 15 6 11 7 L11 10 L6 12 Z M9 13 L25 13 L30 27 H4 Z M17 16 a4.5 4.5 0 1 0 0.01 0 Z" fill="rgba(255,255,255,0.6)" fill-rule="evenodd"/></svg>
      <span>800-555-1212</span>
    </div>
  </section>

  <div class="data-area">
    <span>DATA<br>AREA</span>
  </div>

</main>
</body>
</html>
```